Lanternway 7.5 - Educational Guide/Course-pack/Worksheet

Our Lanternway 7.5 toolkit is an educational workshop that focuses on inspiring student initiatives in the classroom! We need a new educational course guide or course-pack for students/teachers that clearly outlines or explains the program steps, offers helpful tips and includes empty spaces/lines where their can write down their great ideas or notes. This will include a;

- Teachers Guide (1 Page)
- Student Guide/Worksheet (4 Pages)
- Group Pack Resources (3 Pages)

This will consist of designing/formatting text, stock animation/icons, font, etc. We have included our new logo (color, branding, etc.) and all of the text for each separate course-pack. We have also attached our new website to give you an idea of the program style.

Our workshop can be for any school project like Technology, Community, Environment, Art, Science, etc.

Target Market(s)

High School Students/Teachers

Industry/Entity Type

Education

Font styles to use
Sans Serif

Colors
f68e4e
acd037
34a7d8

Requirements
Must have
• Use our brand colors from logo.
Should not have
• Should not be too childish.

```html
<!DOCTYPE html>
<html lang="en">
<head>
<meta charset="UTF-8">
<title>Me and We – Worksheet</title>
<link href="https://fonts.googleapis.com/css2?family=Roboto:ital,wght@0,400;0,500;0,700;1,700;1,900&display=swap" rel="stylesheet">
<style>
  :root {
    --brand-blue: #00a3cc;
    --brand-blue-deep: #0a86a8;
    --brand-green: #acd037;
    --brand-orange: #f68e4e;
    --panel-grey: #e6e7e9;
    --ink: #3a3a3a;
    --muted: #6f6f6f;
    --paper: #fdfdfd;
    --dot: #bdbdbd;
  }
  * { box-sizing: border-box; margin: 0; padding: 0; }
  html, body { width: 849px; height: 1200px; overflow: hidden; background: #fff; }
  body { font-family: "Roboto", sans-serif; color: var(--ink); position: relative; }

  .sheet {
    position: absolute; left: 32px; top: 30px; width: 788px; height: 1139px;
    background: var(--panel-grey);
    border-right: 2px solid var(--brand-blue);
    border-bottom: 7px solid var(--brand-blue);
    border-bottom-right-radius: 44px;
    overflow: hidden;
  }
  .sheet-header {
    position: absolute; left: 0; top: 0; width: 100%; height: 71px;
    background: linear-gradient(90deg, var(--brand-blue-deep), var(--brand-blue) 60%, #04aad3);
  }
  .step-badge {
    position: absolute; left: 0; top: 0; width: 99px; height: 71px;
    background: var(--brand-blue-deep); border-top-left-radius: 30px;
  }
  .step-badge span {
    position: absolute; left: 26px; top: 12px; width: 48px; height: 48px; border-radius: 50%;
    background: #fff; color: var(--brand-blue-deep);
    font: 700 26px/48px "Roboto", sans-serif; text-align: center;
  }
  .sheet-title {
    position: absolute; left: 131px; top: 16px;
    font: italic 900 30px/1 "Roboto", sans-serif; color: #fff; letter-spacing: 0.5px;
  }
  .sheet-title .plain { font-style: normal; font-weight: 700; }

  .section-pill {
    position: absolute; left: 47px; width: 56px; height: 39px; border-radius: 16px;
    background: var(--brand-blue); color: #fff;
    font: italic 900 22px/39px "Roboto", sans-serif; text-align: center;
  }
  .pill-me { top: 96px; }
  .pill-we { top: 524px; }

  .prompt {
    position: absolute; left: 80px; font-size: 15.5px; line-height: 18.5px; color: var(--ink);
  }
  .prompt::before {
    content: ""; position: absolute; left: -20px; top: 0;
    border-left: 12px solid var(--brand-green);
    border-top: 9px solid transparent; border-bottom: 9px solid transparent;
  }
  .prompt-talents { top: 156px; width: 230px; }
  .prompt-think { top: 206px; width: 230px; }
  .prompt-group { top: 582px; width: 600px; }

  .hobby-art {
    position: absolute; left: 65px; top: 313px; width: 272px; height: 220px;
    border-radius: 40px;
    background: radial-gradient(circle at 35% 40%, #c9c4cc, #cfd6d4 55%, transparent 75%),
                radial-gradient(circle at 60% 85%, #e0bba2, transparent 50%);
    opacity: 0.85;
  }

  .notepad {
    position: absolute; left: 336px; top: 132px; width: 396px; height: 394px;
    background: var(--paper); border-radius: 10px;
    box-shadow: 3px 4px 6px rgba(0,0,0,0.12);
  }
  .notepad-rings { position: absolute; left: 0; top: -12px; }
  .notepad-line {
    position: absolute; left: 24px; width: 345px; border-top: 2px dotted #a9a9a9;
  }

  .member-card {
    position: absolute; width: 315px; height: 226px; background: var(--paper);
    border-radius: 8px; box-shadow: 3px 4px 6px rgba(0,0,0,0.12);
  }
  .member-card svg { position: absolute; left: 0; top: 0; }
  .member-card .name-label {
    position: absolute; left: 19px; top: 21px; font-size: 13.5px; font-weight: 500; color: var(--muted);
  }
  .card-a { left: 72px; top: 617px; }
  .card-b { left: 417px; top: 617px; }
  .card-c { left: 72px; top: 871px; }
  .card-d { left: 417px; top: 871px; }
</style>
</head>
<body>
<main class="sheet">
  <header class="sheet-header">
    <div class="step-badge"><span>1</span></div>
    <h1 class="sheet-title">ME <span class="plain">and</span> WE</h1>
  </header>

  <div class="section-pill pill-me">Me</div>
  <p class="prompt prompt-talents">List some of your talents abilities, and interests.</p>
  <p class="prompt prompt-think">Think about private classes, sports, hobbies, music, computers, things you like, things you know how to do.</p>

  <div class="hobby-art" role="img" aria-label="Faded hobby icons: music note, bowling ball, playing card, headphones, chess knight and game controller"></div>

  <section class="notepad">
    <svg class="notepad-rings" width="396" height="40" viewBox="0 0 396 40">
      <g>
        <!-- 18 spiral rings -->
        <g fill="#dcdcdc"><circle cx="28" cy="31" r="7"/><circle cx="48.2" cy="31" r="7"/><circle cx="68.4" cy="31" r="7"/><circle cx="88.6" cy="31" r="7"/><circle cx="108.8" cy="31" r="7"/><circle cx="129" cy="31" r="7"/><circle cx="149.2" cy="31" r="7"/><circle cx="169.4" cy="31" r="7"/><circle cx="189.6" cy="31" r="7"/><circle cx="209.8" cy="31" r="7"/><circle cx="230" cy="31" r="7"/><circle cx="250.2" cy="31" r="7"/><circle cx="270.4" cy="31" r="7"/><circle cx="290.6" cy="31" r="7"/><circle cx="310.8" cy="31" r="7"/><circle cx="331" cy="31" r="7"/><circle cx="351.2" cy="31" r="7"/><circle cx="371.4" cy="31" r="7"/></g>
        <g stroke="var(--brand-green)" stroke-width="3.5" stroke-linecap="round"><line x1="28" y1="2" x2="28" y2="29"/><line x1="48.2" y1="2" x2="48.2" y2="29"/><line x1="68.4" y1="2" x2="68.4" y2="29"/><line x1="88.6" y1="2" x2="88.6" y2="29"/><line x1="108.8" y1="2" x2="108.8" y2="29"/><line x1="129" y1="2" x2="129" y2="29"/><line x1="149.2" y1="2" x2="149.2" y2="29"/><line x1="169.4" y1="2" x2="169.4" y2="29"/><line x1="189.6" y1="2" x2="189.6" y2="29"/><line x1="209.8" y1="2" x2="209.8" y2="29"/><line x1="230" y1="2" x2="230" y2="29"/><line x1="250.2" y1="2" x2="250.2" y2="29"/><line x1="270.4" y1="2" x2="270.4" y2="29"/><line x1="290.6" y1="2" x2="290.6" y2="29"/><line x1="310.8" y1="2" x2="310.8" y2="29"/><line x1="331" y1="2" x2="331" y2="29"/><line x1="351.2" y1="2" x2="351.2" y2="29"/><line x1="371.4" y1="2" x2="371.4" y2="29"/></g>
      </g>
    </svg>
    <div class="notepad-line" style="top:93px"></div>
    <div class="notepad-line" style="top:134px"></div>
    <div class="notepad-line" style="top:174px"></div>
    <div class="notepad-line" style="top:215px"></div>
    <div class="notepad-line" style="top:255px"></div>
    <div class="notepad-line" style="top:296px"></div>
    <div class="notepad-line" style="top:336px"></div>
    <div class="notepad-line" style="top:377px"></div>
  </section>

  <div class="section-pill pill-we">We</div>
  <p class="prompt prompt-group">List the talents, abilities, and interests of each of your group members.</p>

  <svg width="0" height="0" style="position:absolute">
    <defs>
      <g id="card-holes" fill="#e3e3e3">
        <circle cx="26" cy="10" r="5.5"/><circle cx="41.7" cy="10" r="5.5"/><circle cx="57.4" cy="10" r="5.5"/><circle cx="73.1" cy="10" r="5.5"/><circle cx="88.8" cy="10" r="5.5"/><circle cx="104.5" cy="10" r="5.5"/><circle cx="120.2" cy="10" r="5.5"/><circle cx="135.9" cy="10" r="5.5"/><circle cx="151.6" cy="10" r="5.5"/><circle cx="167.3" cy="10" r="5.5"/><circle cx="183" cy="10" r="5.5"/><circle cx="198.7" cy="10" r="5.5"/><circle cx="214.4" cy="10" r="5.5"/><circle cx="230.1" cy="10" r="5.5"/><circle cx="245.8" cy="10" r="5.5"/><circle cx="261.5" cy="10" r="5.5"/><circle cx="277.2" cy="10" r="5.5"/><circle cx="292.9" cy="10" r="5.5"/>
      </g>
    </defs>
  </svg>

  <article class="member-card card-a"><svg width="315" height="20"><use href="#card-holes"/></svg><span class="name-label">Name:</span></article>
  <article class="member-card card-b"><svg width="315" height="20"><use href="#card-holes"/></svg><span class="name-label">Name:</span></article>
  <article class="member-card card-c"><svg width="315" height="20"><use href="#card-holes"/></svg><span class="name-label">Name:</span></article>
  <article class="member-card card-d"><svg width="315" height="20"><use href="#card-holes"/></svg><span class="name-label">Name:</span></article>
</main>
</body>
</html>
```